PowerPoint Design Project

I require a PP design for a project / course I'm creating.
The course is design around Internet marketing and will be called Bright Harvest Method.
I'd like the design to be modern, clean and fresh, with a simple layout.
We will be showcasing videos, images, etc on the slides and be talking around bullet points.
I'd like a page header for each page that is subtle, yet displays the Bright Harvest method logo, and I'd like the ability to add my own copy to the header section for each module we teach.
The simpler the better, less is more as they say, I dont want a cluttered presentation.
Marketing

```html
<!DOCTYPE html>
<html lang="en">
<head>
<meta charset="utf-8">
<title>About Bright Harvest Method</title>
<link rel="stylesheet" href="https://fonts.googleapis.com/css2?family=Exo+2:wght@400;600&family=Open+Sans:wght@400;600&family=Roboto+Condensed:wght@700&display=swap">
<style>
  :root {
    --ink: #2f2f2f;
    --ink-soft: #555555;
    --green: #12a04a;
    --teal: #1b6b70;
    --rule: #c9d7da;
    --footer-line: #19a84e;
    --frame-border: #e6e6e6;
    --frame-fill: #ffffff;
    --band-top: #f4f4f4;
    --band-bottom: #d9d9d9;
  }
  * { box-sizing: border-box; margin: 0; padding: 0; }
  html, body { width: 1200px; height: 900px; overflow: hidden; background: #ffffff; }
  .slide { position: relative; width: 1200px; height: 900px; background: #ffffff; font-family: "Exo 2", sans-serif; color: var(--ink); }

  .slide-header {
    position: absolute; left: 0; top: 0; width: 1200px; height: 102px;
    background: linear-gradient(#ffffff, #f1f1f1);
    border-bottom: 2px solid var(--rule);
  }
  .slide-title { position: absolute; left: 40px; top: 26px; font-size: 42px; font-weight: 400; letter-spacing: 0.5px; }
  .slide-title .accent { color: var(--green); }
  .brand { position: absolute; right: 22px; top: 20px; display: flex; align-items: center; gap: 10px; }
  .brand-dot { width: 40px; height: 40px; border-radius: 50%; background: var(--teal); }
  .brand-name { width: 140px; font-size: 22px; line-height: 24px; font-weight: 600; color: var(--teal); }

  .backdrop-texture {
    position: absolute; left: 700px; top: 104px; width: 500px; height: 500px;
    background: radial-gradient(ellipse at 90% 20%, #efefef 0%, rgba(255,255,255,0) 70%);
  }

  .content { position: absolute; left: 40px; top: 168px; width: 533px; }
  .content-title { font-size: 33px; font-weight: 400; margin-bottom: 20px; }
  .content-title .accent { color: var(--green); }
  .body-copy { font-size: 20px; line-height: 39px; text-align: justify; color: var(--ink-soft); margin-bottom: 39px; }
  .body-copy strong { color: var(--ink); font-weight: 600; }

  .photo-frame {
    position: absolute; left: 682px; width: 446px; height: 198px;
    border: 2px solid var(--frame-border); border-radius: 6px;
    background: var(--frame-fill);
    box-shadow: inset 0 0 10px rgba(0,0,0,0.08), 0 1px 3px rgba(0,0,0,0.06);
    display: flex; align-items: center; justify-content: center;
    font-family: "Open Sans", sans-serif; font-size: 21px; color: #444444;
  }
  .photo-frame.first { top: 237px; }
  .photo-frame.second { top: 507px; }

  .slide-footer {
    position: absolute; left: 0; top: 843px; width: 1200px; height: 57px;
    border-top: 4px solid var(--footer-line);
    background: linear-gradient(var(--band-top), var(--band-bottom));
    font-family: "Roboto Condensed", sans-serif; font-weight: 700; font-size: 21px; color: #333333;
  }
  .page-number { position: absolute; left: 34px; top: 14px; }
  .copyright { position: absolute; right: 36px; top: 14px; }
</style>
</head>
<body>
<div class="slide">
  <div class="backdrop-texture" role="img" aria-label="Faint dotted background texture"></div>

  <header class="slide-header">
    <h1 class="slide-title">About <span class="accent">Bright Harvest Method</span></h1>
    <div class="brand">
      <span class="brand-dot"></span>
      <span class="brand-name">Bright Harvest Method</span>
    </div>
  </header>

  <section class="content">
    <h2 class="content-title">Content <span class="accent">Title Here</span></h2>
    <p class="body-copy"><strong>Lorem ipsum dolor sit ipsum</strong> Lorem ipsum dolor sit ipsum Lorem ipsum Lorem ipsum dolor sit ipsum Lorem ipsum dolor sit ipsum Lorem ipsum.</p>
    <p class="body-copy"><strong>Lorem ipsum dolor sit</strong> ipsum Lorem ipsum dolor sit ipsum Lorem ipsum Lorem ipsum dolor sit ipsum Lorem ipsum dolor sit ipsum Lorem ipsum.</p>
    <p class="body-copy">Lorem ipsum dolor sit ipsum Lorem ipsum dolor sit ipsum Lorem ipsum Lorem ipsum dolor sit ipsum Lorem ipsum dolor sit ipsum Lorem ipsum.</p>
  </section>

  <div class="photo-frame first">Photo Here</div>
  <div class="photo-frame second">Photo Here</div>

  <footer class="slide-footer">
    <span class="page-number">Page No. 00</span>
    <span class="copyright">Copyright@2013</span>
  </footer>
</div>
</body>
</html>
```